The Little Sprouts Forum -Flyer Design

The flyer is for a conference that is being held for Chiropractors to gain continuing education in paediatrics with all proceeds from the event going to paediatric research.

Paediatric chiropractic is mostly about how we can help the body and brain develop optimally with a big focus of the nervous system. I have attached the logo and the website is www.littlesproutsforum.example. The feel should be kid friendly but also professional. It is also going to be largely for the American Market.

Here is an outline of the copy that we need on this flyer:
========================================
Don’t Miss This….some of the best minds in Chiropractic Pediatrics…all together in the USA.

23-24th April 2016, San Francisco. Sat 23rd 8.30-5.30 Sun 24th 8.30am -1pm

Harborview Lodge by Marwell, ​Bayline Terminal-Pierside

With all proceeds going directly to Pediatric based research projects at the Institute for Spinal Wellness Studies at QMPA.

Learn From:

Dr. Marlene Voskuil
Dr. Ingrid Wemkoss
Dr. Fabiola Trennick
Dr. Marianne Pollux
Dr. Terry Vanlund
Dr. Josephine Amsworth
Dr. Lavinia Amsworth
Dr. Greta Pomberg
Dr. Nadia Folck
Dr. Celine Marsh

Early bird $449 18th Mar 2016

CE available

More info at www.littlesproutsforum.example (could we also have a Facebook icon too!)

```html
<!DOCTYPE html>
<html lang="en">
<head>
<meta charset="utf-8">
<title>The Little Sprouts Forum – Flyer</title>
<link href="https://fonts.googleapis.com/css2?family=Bebas+Neue&family=Francois+One&family=Open+Sans:ital,wght@0,400;0,600;0,700;1,700&display=swap" rel="stylesheet">
<style>
  :root{
    --page:#e6e3df;
    --green:#7aa632;
    --green-dark:#5f8a22;
    --orange:#ef6a2a;
    --orange-deep:#e0561c;
    --navy:#14294a;
    --navy-soft:#1d3a63;
    --ink:#222222;
    --white:#ffffff;
    --header-grey:#ececec;
    --fb-blue:#3b5fa8;
  }
  *{box-sizing:border-box;margin:0;padding:0}
  html,body{width:888px;height:1200px;overflow:hidden}
  body{background:var(--page);position:relative;font-family:"Open Sans",Arial,sans-serif}
  .flyer{position:absolute;left:45px;top:83px;width:798px;height:1032px;overflow:hidden;background:var(--white);box-shadow:0 2px 10px rgba(0,0,0,.25)}
  .abs{position:absolute}

  .hero-photo{left:0;top:0;width:798px;height:514px;
    background:linear-gradient(180deg,#b9a48c 0%,#8f7862 45%,#3c2e26 75%,#2a201b 100%)}
  .hero-header{left:0;top:0;width:798px;height:260px}

  .brand{left:36px;top:80px;display:flex;align-items:center;gap:14px}
  .brand-dot{width:46px;height:46px;border-radius:50%;background:var(--orange)}
  .brand-name{font-family:"Open Sans",Arial,sans-serif;font-weight:600;font-size:30px;line-height:1.1;color:var(--orange);width:260px}

  .divider{left:0;top:514px;width:798px;height:4px;background:var(--white)}

  .intro{left:0;top:518px;width:452px;height:133px;background:var(--green);padding:16px 0 0 22px}
  .intro-title{font-family:"Bebas Neue",Impact,sans-serif;font-size:56px;line-height:1;color:var(--white);letter-spacing:1px}
  .intro-sub{font-weight:700;font-size:13.5px;color:var(--orange-deep);margin-top:4px}
  .intro-sub em{display:block;color:var(--ink);font-size:14px}

  .details{left:0;top:651px;width:460px;height:381px;background:linear-gradient(180deg,var(--navy-soft),var(--navy));padding:20px 0 0 22px}
  .dates{font-family:"Bebas Neue",Impact,sans-serif;font-size:38px;line-height:1.06;color:var(--white);letter-spacing:.5px}
  .venue{font-family:"Bebas Neue",Impact,sans-serif;font-size:25px;line-height:1.2;color:var(--green);margin-top:16px;letter-spacing:.5px}
  .note{font-size:13.5px;line-height:1.35;color:var(--white);margin-top:14px;width:360px}

  .side-panel{left:400px;top:518px;width:398px;height:514px}

  .photo-round{border-radius:50%;border:4px solid var(--white);box-shadow:0 0 0 2px var(--navy)}
  .photo-baby{left:442px;top:528px;width:118px;height:118px;background:radial-gradient(circle at 45% 40%,#d8c0a8,#6a5648)}
  .photo-group{left:403px;top:652px;width:150px;height:150px;background:radial-gradient(circle at 50% 40%,#c8a888,#6b5040)}

  .speakers-label{left:577px;top:532px;width:221px;height:45px;background:var(--green);border-radius:10px 0 0 10px;
    font-family:"Francois One",Arial,sans-serif;font-size:30px;line-height:45px;color:var(--white);padding-left:20px}
  .speakers{left:560px;top:585px;width:206px;list-style:none;text-align:right;font-size:15.5px;line-height:22px;color:var(--white)}

  .early-bird{left:468px;top:812px;width:330px;text-align:center;font-family:"Francois One",Arial,sans-serif;font-size:20px;color:var(--navy)}
  .early-bird .price{color:var(--white)}
  .ce-badge{left:518px;top:847px;width:207px;height:38px;border-radius:14px;background:var(--navy);border:2px solid var(--white);
    font-family:"Francois One",Arial,sans-serif;font-size:27px;line-height:33px;text-align:center;color:var(--green)}

  .more-info{left:402px;top:887px;width:396px;height:103px}
  .more-info-text{left:432px;top:896px;width:340px;text-align:right;font-family:"Francois One",Arial,sans-serif;color:var(--ink);font-size:40px;line-height:1.1}
  .more-info-url{left:420px;top:946px;width:352px;text-align:right;font-family:"Francois One",Arial,sans-serif;color:var(--white);font-size:24px}

  .social-square{left:758px;top:998px;width:26px;height:26px;border-radius:4px;background:var(--fb-blue)}
</style>
</head>
<body>
<main class="flyer">

  <div class="abs hero-photo" role="img" aria-label="Photo of a presenter speaking to a seated audience in front of a projection screen"></div>

  <svg class="abs hero-header" viewBox="0 0 798 260" aria-hidden="true">
    <path d="M0 0 H560 C470 70 380 240 260 232 C150 226 60 200 0 170 Z" fill="var(--header-grey)"/>
    <path d="M560 0 C470 70 380 240 260 232 C330 232 420 120 560 40 C640 0 720 0 798 10 V0 Z" fill="var(--green)"/>
    <path d="M798 24 C700 10 620 30 560 60 C640 40 720 50 798 110 Z" fill="var(--orange)"/>
  </svg>

  <div class="abs brand">
    <span class="brand-dot"></span>
    <span class="brand-name">The Little Sprouts Forum</span>
  </div>

  <div class="abs divider"></div>

  <section class="abs intro">
    <h1 class="intro-title">Don’t Miss This….</h1>
    <p class="intro-sub">Some of the best minds in Chiropractic Pediatrics…<em>all together in the USA.</em></p>
  </section>

  <section class="abs details">
    <p class="dates">23-24th April 2016,<br>San Francisco.<br>Sat 23rd 8.30-5.30<br>Sun 24th 8.30am -1pm</p>
    <p class="venue">Harborview Lodge by Marwell,<br>Bayline Terminal-Pierside</p>
    <p class="note">With all proceeds going directly to Pediatric based research projects at the Institute for Spinal Wellness Studies at QMPA.</p>
  </section>

  <svg class="abs side-panel" viewBox="0 0 398 514" aria-hidden="true">
    <path d="M100 0 H398 V514 H120 C60 420 50 300 70 180 C80 110 90 50 100 0 Z" fill="var(--white)"/>
    <path d="M112 0 H398 V514 H134 C74 420 64 300 84 180 C94 110 102 50 112 0 Z" fill="var(--orange)"/>
  </svg>

  <div class="abs photo-round photo-baby" role="img" aria-label="Photo of a baby looking upward"></div>
  <div class="abs photo-round photo-group" role="img" aria-label="Photo of the speaker group standing together"></div>

  <h2 class="abs speakers-label">Learn From:</h2>
  <ul class="abs speakers">
    <li>Dr. Marlene Voskuil</li>
    <li>Dr. Ingrid Wemkoss</li>
    <li>Dr. Fabiola Trennick</li>
    <li>Dr. Marianne Pollux</li>
    <li>Dr. Terry Vanlund</li>
    <li>Dr. Josephine Amsworth</li>
    <li>Dr. Lavinia Amsworth</li>
    <li>Dr. Greta Pomberg</li>
    <li>Dr. Nadia Folck</li>
    <li>Dr. Celine Marsh</li>
  </ul>

  <p class="abs early-bird">Early bird <span class="price">$449</span> 18th Mar 2016</p>
  <p class="abs ce-badge">CE available</p>

  <svg class="abs more-info" viewBox="0 0 396 103" aria-hidden="true">
    <path d="M0 0 H396 V103 H14 V22 Z" fill="var(--green)"/>
    <path d="M0 0 L14 22 V14 Z" fill="var(--green-dark)"/>
  </svg>
  <p class="abs more-info-text">More info at</p>
  <p class="abs more-info-url">www.littlesproutsforum.example</p>

  <span class="abs social-square"></span>
</main>
</body>
</html>
```